Web design for new streaming audio service

We need a homepage design for a new streaming audio service. Our company is called Olvantra, and we’re basically Vidorama for Audiobooks, Stand-Up Comedy, Lectures, Language Learning, etc. Essentially like Tunelark for everything audio EXCEPT music.
You don’t have to code the homepage (Design Only), but it should include 3 different designs to work with 1) Web; 2) Phones; 3) Tablets.
Below is a link to a mockup of the web version which gives a good idea of what elements we want. This is just a mockup and we want you to improve it.
Once you download the mockup, please refer to the more detailed instructions below:
The following outlines the design project for the Olvantra homepage. We have provided a rough mockup of the homepage layout that gives you a general idea of what we’re going for. There are a few elements that we are attached to, and many others where you have complete creative freedom to do whatever you think looks good.
The ZIP file includes the following:
* Mockup to see what we have in mind (olvantra-homepage-mockup.jpg)
* Text used (olvantra-homepage-text.txt)
* Raw image of actor (olvantra-actor1.jpg)
* Raw images for samples (olvantra-sample-[name].jpg)
Although we have only provided a mockup layout for the web version, we also need you to provide a mobile phone and a tablet version of the design also. It’s very possible the tablet version may be substantially similar to the web version, but the mobile phone version will likely be much different.
All of the raw files are included in the attached ZIP file. Please use our photographs and text as provided although cropping, sizing, etc. is flexible per the instructions below.
Display Requirements:
* Web Version - Minimum resolution 1024x768 (72 dpi) but should look good on 1920x1080 (72 dpi) - Page should be designed to scale to look acceptable in all resolutions in between.
* Phone Version - Minimum Zentro 4 - 640x960 (326 dpi) but should look good on Korvel Nimbus Q5 - 1920x1080 (441 dpi) - Page should be designed to scale to look acceptable in all resolutions and devices in between.
* Tablet Version - Minimum Pagewick Ember LX 7” - 1280x800 (216 dpi) but should also look good on a Slato Breeze - 2048x1536 (264 dpi) - Page should be designed to scale to look acceptable in all resolutions and devices in between.
Above the Fold - We want to make sure the Olvantra logo, Member Login Link, Large Photo, Headline, Price, Button, and the first row of sample images are all “Above the fold”. As a general guideline, this means 600 pixels high on a 1024x768 72 dpi web screen. This requirement is less important on Phone versions.
Top Logo Bar - We want to retain the blue bar with the Olvantra logo on the page, although we are open to a different size, shape and positioning if it greatly enhances the design. Please use the standard logo color, although you are welcome to use either the horizontal or vertical orientation of the logo based on your design.
Text color, font and size - Feel free to design the text in anyway you choose as long as the text is readable on the target platforms.
Buttons - Feel free to use any size, shape and colors for the buttons as long as they are obvious and clickable relative to the page. The only exception is the Chatterly button should follow the Chatterly color scheme and logo treatment (the mockup doesn’t seem 100% correct.)
Top Photograph - We want to retain the large photograph across the top of the screen although final shape and dimensions are flexible.
Size and shape of content samples (i.e. Audiobooks, Stand-Up Comedy, etc.) - Feel free to design the content samples in anyway you choose.
Three Sales Points (i.e. Listen on your Zentro…, All you can enjoy…, etc.) - The Three Sales Points are envisioned to each have a corresponding illustration which you should provide and have rights for. The placeholder is represented by a square next to the text. The color size and shape of these elements are flexible and can be designed in any way you choose.
Opt-in form - Feel free to design the opt-in form in anyway you choose as long as the text is readable and the interactivity is obvious on the target platforms.
Text links and copyright notice - Feel free to design the bottom of the page text links and copyright notice in anyway you choose.
Additional colors, graphic design elements, etc. - Feel free to use any additional colors, graphic design elements, etc. to support your design.

```html
<!DOCTYPE html>
<html lang="en">
<head>
<meta charset="utf-8">
<title>Olvantra – Unlimited Listening</title>
<link rel="stylesheet" href="https://fonts.googleapis.com/css2?family=Oswald:wght@300;400&family=Jost:wght@300;400;500&family=Open+Sans:wght@400;600;700&display=swap">
<style>
  :root {
    --sky: #5aa9d6;
    --sky-dark: #4f9cc9;
    --brick: #d9493f;
    --coral: #e05a4b;
    --coral-deep: #d2463a;
    --orange: #f0862f;
    --violet: #a584bd;
    --ink: #2b2b2b;
    --grey-text: #555;
    --panel: #eeeeee;
    --white: #ffffff;
    --social: #3d5a98;
  }
  * { box-sizing: border-box; margin: 0; padding: 0; }
  html, body { width: 1200px; height: 2192px; overflow: hidden; }
  body {
    position: relative;
    background: var(--white);
    font-family: "Open Sans", Arial, sans-serif;
    color: var(--ink);
  }
  .abs { position: absolute; }

  /* Top bar */
  .topbar { left: 0; top: 0; width: 1200px; height: 81px; background: var(--sky); }
  .brand {
    left: 188px; top: 16px; height: 48px;
    display: flex; align-items: center; gap: 12px;
    font-family: "Jost", sans-serif; font-weight: 500; font-size: 38px; color: var(--white);
  }
  .brand-dot { width: 36px; height: 36px; border-radius: 50%; background: var(--white); }
  .login-btn {
    left: 852px; top: 19px; width: 158px; height: 42px; background: var(--brick);
    display: flex; align-items: center; justify-content: center; gap: 8px;
    font-size: 12px; font-weight: 700; color: var(--white); letter-spacing: .3px;
  }

  /* Hero */
  .hero-photo {
    left: 0; top: 81px; width: 1200px; height: 652px;
    background: linear-gradient(100deg, #f2f3f4 0%, #e6e4e1 35%, #c9a58a 55%, #7a6a62 75%, #4c5466 100%);
  }
  .headline {
    left: 185px; top: 222px; font-family: "Oswald", sans-serif; font-weight: 400;
    font-size: 50px; color: #d9553f; letter-spacing: .5px; line-height: 1;
  }
  .subhead {
    left: 187px; top: 280px; font-family: "Jost", sans-serif; font-weight: 300;
    font-size: 31px; color: #222; letter-spacing: .5px; line-height: 1;
  }
  .price {
    left: 186px; top: 320px; font-family: "Oswald", sans-serif; font-weight: 300;
    font-size: 38px; color: var(--sky); line-height: 1;
  }
  .trial-btn {
    left: 188px; top: 378px; width: 201px; height: 40px; background: var(--orange);
    display: flex; align-items: center; justify-content: center;
    font-size: 13px; font-weight: 700; color: var(--white);
  }
  .trial-note { left: 238px; top: 421px; font-size: 12px; font-weight: 600; color: #111; }

  /* Samples */
  .samples-title {
    left: 186px; top: 788px; font-family: "Jost", sans-serif; font-weight: 300;
    font-size: 28px; color: #555;
  }
  .tile { width: 201px; height: 201px; }
  .tile-audiobooks {
    background: var(--sky); display: flex; flex-direction: column;
    align-items: center; justify-content: center; gap: 10px;
    color: var(--white); font-family: "Jost", sans-serif; font-weight: 500; font-size: 18px;
  }
  .cover-comedy { background: linear-gradient(160deg, #b7a98f, #6e5e4d); }
  .cover-language { background: linear-gradient(180deg, #111 0 14%, #3fa9e0 14% 100%); }
  .cover-memoir { background: linear-gradient(180deg, #8c8477 0 78%, #7cbb5e 78% 100%); }
  .cover-relax { background: linear-gradient(180deg, #c04fa8 0%, #8a3a8e 55%, #4d2a5e 100%); }
  .cover-wealth { background: linear-gradient(160deg, #2b2015, #6b4a22 60%, #1a1a1a); }
  .cover-pop { background: linear-gradient(150deg, #3a2a26, #c06a6a 55%, #e8a060); }
  .cover-fitness { background: linear-gradient(160deg, #5fc4ec, #2a9fd8); }

  /* Studio banner */
  .studio {
    left: 0; top: 1318px; width: 1200px; height: 285px;
    background: radial-gradient(ellipse at 30% 40%, #3a9bd0 0%, #1f6fa5 45%, #0e3d66 100%);
  }
  .studio-lead {
    left: 186px; top: 1405px; width: 660px; font-size: 25px; line-height: 1.35; color: var(--white);
  }
  .studio-tag { left: 186px; top: 1488px; font-size: 20px; color: var(--white); }
  .watch-ring {
    left: 886px; top: 1399px; width: 122px; height: 122px; border-radius: 50%;
    border: 2px solid var(--white); display: flex; align-items: center; justify-content: center;
    text-align: center; font-size: 15px; line-height: 1.3; color: var(--white);
  }

  /* Sales points */
  .point {
    top: 1658px; width: 265px; height: 183px; background: var(--panel);
    display: flex; flex-direction: column; align-items: center;
  }
  .point-icon {
    margin-top: 19px; width: 100px; height: 100px; border-radius: 50%;
    display: flex; align-items: center; justify-content: center;
  }
  .point-text {
    margin-top: 16px; width: 210px; text-align: center; font-size: 12.5px; line-height: 1.4; color: #333;
  }
  .point-devices { left: 186px; border-bottom: 4px solid var(--sky); }
  .point-devices .point-icon { background: var(--sky); }
  .point-price { left: 467px; border-bottom: 4px solid var(--violet); }
  .point-price .point-icon { background: var(--violet); }
  .point-cancel { left: 747px; border-bottom: 4px solid var(--orange); }
  .point-cancel .point-icon { background: #ec8f5a; }

  /* Signup */
  .signup { left: 0; top: 1893px; width: 1200px; height: 227px; background: var(--coral); }
  .signup-title {
    left: 186px; top: 1932px; font-family: "Jost", sans-serif; font-weight: 400;
    font-size: 24px; color: var(--white);
  }
  .signup-copy {
    left: 186px; top: 1980px; width: 300px; font-size: 14px; line-height: 1.45; color: var(--white);
  }
  .signup-note { left: 186px; top: 2074px; font-size: 12px; font-weight: 600; color: #222; }
  .email-field {
    left: 642px; top: 1957px; width: 315px; height: 54px; background: var(--white);
    display: flex; align-items: center; padding-left: 15px; font-size: 13px; color: #999;
  }
  .email-go {
    left: 959px; top: 1957px; width: 51px; height: 54px; background: var(--white);
    display: flex; align-items: center; justify-content: center;
  }
  .access-btn {
    left: 642px; top: 2037px; width: 173px; height: 53px; background: var(--orange);
    display: flex; align-items: center; justify-content: center;
    font-size: 15px; font-weight: 600; color: var(--white);
  }
  .or-label { left: 818px; top: 2053px; font-size: 14px; font-weight: 600; color: var(--white); }
  .social-btn {
    left: 838px; top: 2037px; width: 172px; height: 53px; background: var(--social);
    display: flex; align-items: center; justify-content: center;
    font-size: 12px; font-weight: 600; color: var(--white);
  }

  /* Footer */
  .footer { left: 0; top: 2120px; width: 1200px; height: 72px; background: var(--coral-deep); }
  .footer-links { left: 186px; top: 2146px; font-size: 11px; color: var(--white); }
  .copyright { left: 800px; top: 2146px; width: 210px; text-align: right; font-size: 11px; color: var(--white); }
</style>
</head>
<body>

<header>
  <div class="abs topbar"></div>
  <div class="abs brand"><span class="brand-dot"></span>Olvantra</div>
  <div class="abs login-btn">
    <svg width="14" height="14" viewBox="0 0 14 14"><circle cx="7" cy="4" r="3.2" fill="#fff"/><path d="M1 14c0-4 2.7-6 6-6s6 2 6 6z" fill="#fff"/></svg>
    MEMBER LOGIN
  </div>
</header>

<section class="hero">
  <div class="abs hero-photo" role="img" aria-label="Smiling young man wearing headphones listening on his phone"></div>
  <h1 class="abs headline">UNLIMITED LISTENING.</h1>
  <p class="abs subhead">WHEREEVER YOU ARE</p>
  <p class="abs price">Only $9.99 per month</p>
  <div class="abs trial-btn">START YOUR FREE TRIAL</div>
  <p class="abs trial-note">* Credit Card Not Required</p>
</section>

<section class="samples">
  <h2 class="abs samples-title">A sample of what you can listen to on Olvantra</h2>
  <div class="abs tile tile-audiobooks" style="left:186px;top:846px;">
    <svg width="56" height="44" viewBox="0 0 56 44" fill="none" stroke="#fff" stroke-width="3">
      <path d="M4 8c8-3 16-3 22 2v30c-6-5-14-5-22-2z"/>
      <path d="M48 8c-8-3-16-3-22 2v30c6-5 14-5 22-2z"/>
    </svg>
    Audiobooks
  </div>
  <div class="abs tile cover-comedy" style="left:393px;top:846px;" role="img" aria-label="Stand-up comedy album cover with a boxer illustration"></div>
  <div class="abs tile cover-language" style="left:603px;top:846px;" role="img" aria-label="French language learning course cover"></div>
  <div class="abs tile cover-memoir" style="left:812px;top:846px;" role="img" aria-label="Biography audiobook cover with a portrait"></div>
  <div class="abs tile cover-relax" style="left:186px;top:1054px;" role="img" aria-label="Relaxation audio cover with purple mountains"></div>
  <div class="abs tile cover-wealth" style="left:393px;top:1054px;" role="img" aria-label="Wealth building lecture cover"></div>
  <div class="abs tile cover-pop" style="left:603px;top:1054px;" role="img" aria-label="Pop star biography audiobook cover"></div>
  <div class="abs tile cover-fitness" style="left:812px;top:1054px;" role="img" aria-label="Elliptical workout coaching audio cover"></div>
</section>

<section class="studio-band">
  <div class="abs studio" role="img" aria-label="Blue soft-focus light background"></div>
  <p class="abs studio-lead">As a creative studio we believe no client is too big nor too small to work with us.</p>
  <p class="abs studio-tag">We love what we do. And that shows.</p>
  <div class="abs watch-ring">WATCH<br>US WORK</div>
</section>

<section class="points">
  <div class="abs point point-devices">
    <div class="point-icon">
      <svg width="50" height="50" viewBox="0 0 50 50" fill="none" stroke="#fff" stroke-width="3">
        <rect x="6" y="6" width="26" height="38" rx="3"/>
        <rect x="34" y="20" width="12" height="24" rx="2"/>
      </svg>
    </div>
    <p class="point-text">LISTEN ON YOUR ZENTRO, SLATO OR ROBIX DEVICE.</p>
  </div>
  <div class="abs point point-price">
    <div class="point-icon">
      <svg width="50" height="50" viewBox="0 0 50 50"><text x="25" y="38" text-anchor="middle" font-family="Open Sans, sans-serif" font-weight="700" font-size="38" fill="#fff">$</text></svg>
    </div>
    <p class="point-text">ALL YOU CAN ENJOY FOR ONE LOW MONTHLY PRICE.</p>
  </div>
  <div class="abs point point-cancel">
    <div class="point-icon">
      <svg width="54" height="54" viewBox="0 0 54 54" stroke="#fff" stroke-width="6" stroke-linecap="round">
        <path d="M10 44L44 10M12 12c8 6 18 16 30 32"/>
      </svg>
    </div>
    <p class="point-text">NO OBLIGATION. CANCEL ANY TIME.</p>
  </div>
</section>

<section class="signup-band">
  <div class="abs signup"></div>
  <h2 class="abs signup-title">Start Your Free Trial</h2>
  <p class="abs signup-copy">You will get instant &amp; unlimited access to all the material on Olvantra for 14 days. There is no obligation &amp; you can cancel at any time.</p>
  <p class="abs signup-note">Credit Card Not Required for Free Trial</p>
  <div class="abs email-field">Your Email Address</div>
  <div class="abs email-go">
    <svg width="16" height="20" viewBox="0 0 16 20" fill="none" stroke="#aaa" stroke-width="1.5"><path d="M3 2l10 8-10 8"/></svg>
  </div>
  <div class="abs access-btn">Get Instant Access</div>
  <span class="abs or-label">Or</span>
  <div class="abs social-btn">Sign Up Using Chatterly</div>
</section>

<footer>
  <div class="abs footer"></div>
  <p class="abs footer-links">About &nbsp;|&nbsp; Help &nbsp;|&nbsp; Contact Us &nbsp;|&nbsp; Member Login &nbsp;|&nbsp; Privacy Policy &nbsp;|&nbsp; Terms of Service</p>
  <p class="abs copyright">©2014 Olvantra LLC - All Rights Reserved</p>
</footer>

</body>
</html>
```